Veltrix Hand Sanitiser Spray Product Range for International Markets

Veltrix is a new Healthcare business launching a full product range of Anti-bacterial Hand Sanitiser Spray bottles in various sizes. We have a new logo which we believe differentiates us from the competition: Veltrix - Care That Stays With You
The Product Range will comprise two distinct product solution types:
- Anti-bacterial Hand Sanitisers - Alcohol based
- Anti-bacterial Hand Sanitisers - Sensitive Non Alcohol based
Bottle sizes will comprise a range containing:
100ml, 250ml, 500ml, 1ltr, 5ltr, 10ltr
Some bottles will have Pump Sprays
The Product labelling will be attractive front packaging label combined with strong product attributes and usage indicator cues.
As a Healthcare brand our logo design is light Green. We believe that this should be combined with blues and greens balanced to create contrast and strong stand-out on-shelf.
A review of competitor brands will show some similar colour cues, however as a Healthcare brand, the colour cues Green and White are synonymous with the sector. Many existing brands are very pragmatic in their label design. i.e. #it does what is says on the tin approach#. Our brand will need strong stand-out and strong aesthetic appeal too, since it will often be left in public view and around the home and office and therefore should look as attractive as possible. There will be other brand variants in the future and thought should be given to this too - with use of colour cues.
For Competitor indicators check-out the brands on Shopvale - Birch Lane, Dermalux and others....Thank-you!

Target Market(s)

First: Female 25 - 65
Second: Male 25 - 65

Contact Information for Business Card

Greg T. Hollis
CEO
Veltrix Healthcare International
'Care That Stays With You'
www.VeltrixHealthcare.example
E. gthollis@veltrixhealthcare.example
T. +44 7700 900312
T. +44 118 496051

Font styles to use
Sans Serif

Colors
34a7d7
33b8a4
add136
fbee3e
b768aa

```html
<!DOCTYPE html>
<html lang="en">
<head>
<meta charset="utf-8">
<title>Veltrix Hand Sanitizer Label</title>
<link href="https://fonts.googleapis.com/css2?family=Bebas+Neue&family=Figtree:wght@400;500;800&display=swap" rel="stylesheet">
<style>
  :root {
    --brand-green: #45b34a;
    --label-white: #ffffff;
    --backdrop: #f1f3f1;
  }
  html, body {
    margin: 0;
    padding: 0;
    width: 800px;
    height: 1200px;
    overflow: hidden;
    background: var(--backdrop);
  }
  .canvas {
    position: relative;
    width: 800px;
    height: 1200px;
  }
  .label {
    position: absolute;
    left: 110px;
    top: 165px;
    width: 580px;
    height: 870px;
    background: var(--label-white);
    overflow: hidden;
  }
  .label__wave {
    position: absolute;
    inset: 0;
    width: 580px;
    height: 870px;
  }
  .label__wave path { fill: var(--brand-green); }
  .brand {
    position: absolute;
    left: 0;
    right: 0;
    text-align: center;
    color: var(--brand-green);
    font-family: "Figtree", sans-serif;
  }
  .brand__name {
    top: 104px;
    font-size: 104px;
    font-weight: 500;
    line-height: 1;
    letter-spacing: -1px;
  }
  .brand__tagline {
    top: 208px;
    font-size: 15px;
    font-weight: 400;
    line-height: 1;
    letter-spacing: 5px;
    padding-left: 5px;
  }
  .product {
    position: absolute;
    left: 0;
    right: 0;
    text-align: center;
    color: var(--label-white);
    line-height: 1;
  }
  .product__claim {
    top: 444px;
    font-family: "Figtree", sans-serif;
    font-size: 35px;
    font-weight: 400;
    left: 20px;
  }
  .product__name {
    font-family: "Bebas Neue", sans-serif;
    font-size: 128px;
    letter-spacing: 1px;
  }
  .product__name--hand { top: 480px; left: 20px; }
  .product__name--sanitizer { top: 593px; left: 20px; }
  .product__rule {
    position: absolute;
    left: 171px;
    width: 261px;
    height: 6px;
    background: var(--label-white);
  }
  .product__rule--top { top: 713px; }
  .product__rule--bottom { top: 763px; }
  .product__type {
    top: 726px;
    left: 20px;
    font-family: "Figtree", sans-serif;
    font-size: 33px;
    font-weight: 400;
  }
  .product__volume {
    top: 812px;
    font-family: "Figtree", sans-serif;
    font-size: 33px;
    font-weight: 800;
  }
</style>
</head>
<body>
<main class="canvas">
  <section class="label">
    <svg class="label__wave" viewBox="0 0 580 870" aria-hidden="true">
      <path d="M0 471 C80 472 170 410 230 370 C290 330 330 328 380 348 C420 364 440 385 470 377 C520 362 540 300 580 268 L580 870 L0 870 Z"/>
    </svg>

    <div class="brand brand__name">Veltrix</div>
    <div class="brand brand__tagline">CARE THAT STAYS WITH YOU</div>

    <div class="product product__claim">ANTI-BACTERIAL</div>
    <div class="product product__name product__name--hand">HAND</div>
    <div class="product product__name product__name--sanitizer">SANITIZER</div>
    <div class="product__rule product__rule--top"></div>
    <div class="product product__type">ALCOHOL BASED</div>
    <div class="product__rule product__rule--bottom"></div>
    <div class="product product__volume">100ml</div>
  </section>
</main>
</body>
</html>
```